Australian Meat, Seafood and Fresh Produce Website

Our organization is looking to design a simple, but eye catching website to show our services.
Our company exports West Australian FRESH fruit and vegetables, seafood and meat.
The website we are looking for would consist of:
- Landing Page
- Company info
- Directors bio
- Page that highlights our products
- Contact us page
We would like it to have a Chinese translated version as well.
Tobin
Target Market(s)
Chinese Market
Industry/Entity Type
It Company
Number of Pages Required
1 page
Look and feel
Each slider illustrates characteristics of the customer's brand and the style your logo design should communicate.

```html
<!DOCTYPE html>
<html lang="en">
<head>
<meta charset="utf-8">
<title>Greenvale – West Australian Fresh Produce</title>
<link href="https://fonts.googleapis.com/css2?family=Montserrat:wght@400;600;700&family=Open+Sans:wght@400;600;700&display=swap" rel="stylesheet">
<style>
:root{
  --green:#8cc63f;
  --green-dark:#2f4a1e;
  --orange:#f7941d;
  --yellow:#f9b518;
  --lime:#8dc63f;
  --teal:#3ec5a5;
  --ink:#333;
  --muted:#888;
  --line:#e4e4e4;
  --paper:#fff;
  --footer:#f2f2f2;
}
*{box-sizing:border-box;margin:0;padding:0}
html,body{width:1200px;height:2840px;overflow:hidden}
body{background:var(--paper);font-family:"Open Sans",Arial,sans-serif;color:var(--ink);font-size:12px;position:relative}
.abs{position:absolute}
.section-title{position:absolute;left:0;width:1200px;text-align:center;font-family:"Montserrat",Arial,sans-serif;font-weight:700;font-size:20px;letter-spacing:1px;color:#3a3a3a;line-height:24px}
.section-rule{position:absolute;left:240px;width:720px;height:1px;background:var(--line)}
.section-rule span{position:absolute;left:240px;top:-10px;width:240px;height:20px;background:var(--paper)}

/* hero */
.hero{left:0;top:0;width:1200px;height:400px;background:radial-gradient(circle at 12% 40%,#b8321d 0,#7a2a12 18%,transparent 32%),radial-gradient(circle at 90% 35%,#c23d22 0,#6b2410 18%,transparent 30%),linear-gradient(180deg,#3b2a1a,#5a3f26 60%,#2c1e12)}
.logo{left:240px;top:20px;width:180px;height:44px;background:var(--green-dark);color:#fff;font-family:"Montserrat",sans-serif;font-weight:700;font-size:20px;display:flex;align-items:center;justify-content:center}
.nav{left:420px;top:20px;width:460px;height:44px;background:var(--paper);display:flex}
.nav a{flex:1;display:flex;align-items:center;justify-content:center;font-family:"Montserrat",sans-serif;font-size:10px;font-weight:600;color:#555;text-decoration:none;white-space:nowrap}
.nav a.active{flex:1.3;background:var(--green);color:#fff}
.social{top:24px;width:34px;height:34px;border-radius:50%;background:#fff;display:flex;align-items:center;justify-content:center}
.mega{left:240px;top:64px;width:704px;height:236px;background:var(--paper);box-shadow:0 4px 12px rgba(0,0,0,.25)}
.mega-col{position:absolute;top:18px;width:120px}
.mega-col h4{font-family:"Montserrat",sans-serif;font-size:10px;font-weight:700;color:#444;padding-bottom:8px;border-bottom:1px solid var(--line);margin-bottom:6px}
.mega-col li{list-style:none;font-size:10px;color:var(--muted);line-height:22px}
.mega-photo{left:544px;top:18px;width:150px;height:170px;background:linear-gradient(135deg,#e9a23b,#8b5a2b 55%,#5e9b2f)}
.mega-btn{left:584px;top:200px;width:110px;height:26px;background:var(--green);color:#fff;font-size:10px;font-weight:700;display:flex;align-items:center;justify-content:center}

/* features */
.feature{top:400px;width:176px;height:240px;color:#fff;padding:22px 16px}
.feature h3{font-family:"Montserrat",sans-serif;font-size:19px;font-weight:700;line-height:24px}
.feature .sub{font-size:13px;opacity:.9;margin-bottom:14px}
.feature p{font-size:10px;line-height:16px;opacity:.9}
.feature .more{position:absolute;bottom:22px;left:16px;font-size:10px;font-weight:700}

/* products */
.subtitle{position:absolute;left:0;width:1200px;text-align:center;font-size:10px;color:var(--muted);letter-spacing:1px}
.product{top:800px;width:158px;height:300px;text-align:center;padding-top:20px}
.product.featured{border:1px solid #d5d5d5;box-shadow:0 2px 8px rgba(0,0,0,.08)}
.product .photo{margin:0 auto;width:120px;height:110px;border-radius:8px}
.product h5{font-size:11px;margin-top:30px;font-weight:600}
.stars{color:var(--yellow);font-size:12px;letter-spacing:1px}
.price{color:var(--orange);font-weight:700;font-size:14px}
.product .btns{display:flex;justify-content:center;gap:4px;margin-top:12px}
.product .btns span{width:42px;height:22px;background:var(--orange);color:#fff;font-size:8px;display:flex;align-items:center;justify-content:center}
.product .btns span+span{background:#ccc}
.arrow{top:930px;width:22px;height:22px;background:#ddd;display:flex;align-items:center;justify-content:center}

/* news */
.news{top:1188px;width:236px;height:132px;display:flex}
.news .date{width:56px;color:#fff;font-family:"Montserrat",sans-serif;font-weight:700;font-size:22px;padding:10px 8px;line-height:1}
.news .date small{display:block;font-size:10px;font-weight:400}
.news .photo{flex:1}
.news-text{flex:1;color:#fff;padding:14px 10px;font-size:10px;line-height:15px}

/* achievements */
.card{border:1px solid #dcdcdc;background:var(--paper)}
.member{left:248px;top:1424px;width:168px;height:280px;text-align:center;padding-top:34px}
.member .avatar{width:84px;height:84px;border-radius:50%;background:var(--orange);margin:0 auto}
.btn{background:var(--orange);color:#fff;font-size:10px;font-weight:700;display:inline-flex;align-items:center;justify-content:center;height:24px;padding:0 14px}
.tabs{left:440px;top:1424px;width:320px;height:280px}
.tabs .tabbar{display:flex;height:28px;margin:0 20px}
.tabs .tabbar span{flex:1;display:flex;align-items:center;justify-content:center;font-size:10px;background:#eee;border-right:1px solid #ddd}
.tabs .tabbar span.on{background:var(--green);color:#fff}
.tabs .body{padding:12px 20px}
.tabs h4{font-family:"Montserrat",sans-serif;font-size:14px;font-weight:600;line-height:19px}
.tabs h4.small{font-size:12px;line-height:16px}
.count{font-family:"Montserrat",sans-serif;font-size:26px;font-weight:600;letter-spacing:2px;margin-top:10px;line-height:32px}
.count-lbl{display:flex;gap:30px;font-size:9px;color:var(--muted);margin-bottom:10px}
.tabs p{font-size:10px;color:var(--muted);line-height:15px}
.tabs p.link{margin-top:8px;color:var(--ink);font-weight:600}
.offer{left:792px;top:1424px;width:164px;height:280px;text-align:center;padding-top:26px}
.offer h4{font-size:15px;font-weight:400;color:#555;line-height:20px}
.offer .big{color:var(--orange);font-family:"Montserrat",sans-serif;font-size:32px;font-weight:700;margin:14px 0}
.offer ul{list-style:none;text-align:left;padding-left:22px;font-size:9px;color:var(--muted);line-height:17px;margin-bottom:16px}

/* best products */
.best{top:1830px;width:228px;height:172px;color:#fff;padding:14px}
.best h4{font-size:11px;font-weight:700}
.best .tag{font-family:"Montserrat",sans-serif;font-size:26px;font-weight:700;margin-top:4px}
.best .photo{position:absolute;left:60px;right:10px;bottom:10px;height:100px;border-radius:8px}

/* partners */
.partner{top:2128px;width:140px;height:44px;background:#d9d9d9;border-radius:22px}

/* banner */
.banner{left:0;top:2240px;width:1200px;height:220px;background:radial-gradient(circle at 20% 60%,#c1361f,#7b2713 30%,transparent 45%),radial-gradient(circle at 80% 50%,#6f9d2e,#3e6418 35%,transparent 55%),linear-gradient(180deg,#4b5a24,#2f3a16)}
.banner-title{position:absolute;left:0;top:2290px;width:1200px;text-align:center;font-family:"Montserrat",sans-serif;font-weight:700;font-size:34px;color:#fff;line-height:40px}
.banner-btn{left:530px;top:2354px;width:140px;height:32px;border:2px solid #fff;color:#fff;font-size:10px;font-weight:700;display:flex;align-items:center;justify-content:center}

/* tweet */
.tweet{left:240px;top:2492px;width:720px;display:flex;gap:12px;font-size:10px;color:var(--muted);line-height:14px}

/* footer */
.footer{left:0;top:2544px;width:1200px;height:296px;background:var(--footer)}
.fcol{top:2570px;width:170px}
.fcol h5{font-family:"Montserrat",sans-serif;font-size:10px;color:var(--orange);font-weight:700;padding-bottom:8px;border-bottom:1px solid #ddd;margin-bottom:8px}
.fcol li{list-style:none;font-size:10px;color:var(--muted);line-height:22px;border-bottom:1px solid #e6e6e6}
.copy{left:240px;top:2806px;font-size:9px;color:var(--muted)}
</style>
</head>
<body>

<!-- hero -->
<div class="abs hero" role="img" aria-label="Photo of fresh tomatoes, peppers and vegetables on a wooden table"></div>
<div class="abs logo">Greenvale</div>
<nav class="abs nav">
  <a>HOME</a><a>ABOUT US</a><a>SHOP</a><a class="active">VEGETABLES</a><a>DELIVERY</a><a>CONTACT</a>
</nav>
<div class="abs social" style="left:900px"><svg width="12" height="12" viewBox="0 0 12 12"><circle cx="6" cy="6" r="4" fill="none" stroke="#555" stroke-width="1.5"/></svg></div>
<div class="abs social" style="left:942px"><svg width="12" height="12" viewBox="0 0 12 12"><rect x="2" y="2" width="8" height="8" fill="none" stroke="#555" stroke-width="1.5"/></svg></div>

<div class="abs mega">
  <div class="mega-col" style="left:24px"><h4>VEGETABLES</h4><ul><li>Carrots</li><li>Sweet Potato</li><li>Broccoli</li><li>Potato</li><li>Cabbage</li><li>Spinach</li></ul></div>
  <div class="mega-col" style="left:154px"><h4>FRUITS</h4><ul><li>Strawberry</li><li>Mango</li><li>Avocado</li><li>Apple</li><li>Orange</li><li>Banana</li></ul></div>
  <div class="mega-col" style="left:284px"><h4>SEA FOOD</h4><ul><li>Prawns</li><li>Rock Lobster</li><li>Oysters</li><li>Scallops</li><li>Crab</li><li>Snapper</li></ul></div>
  <div class="mega-col" style="left:414px"><h4>MEAT</h4><ul><li>Beef</li><li>Lamb</li><li>Pork</li><li>Chicken</li><li>Goat</li><li>Veal</li></ul></div>
  <div class="abs mega-photo" role="img" aria-label="Photo of a wooden crate full of vegetables"></div>
  <div class="abs mega-btn">SHOP NOW</div>
</div>

<!-- features -->
<div class="abs feature" style="left:248px;background:var(--orange)"><h3>Best Price</h3><div class="sub">Delivery</div><p>Fair prices from farm to port with fast reliable delivery.</p><div class="more">Read More »</div></div>
<div class="abs feature" style="left:424px;background:var(--yellow)"><h3>Premium</h3><div class="sub">Quality</div><p>Hand picked produce graded to the highest export standard.</p><div class="more">Read More »</div></div>
<div class="abs feature" style="left:600px;background:var(--lime)"><h3>Organic</h3><div class="sub">100% Healthy</div><p>Grown in clean West Australian soil without harsh chemicals.</p><div class="more">Read More »</div></div>
<div class="abs feature" style="left:776px;background:var(--teal)"><h3>Shipping</h3><div class="sub">Free</div><p>Chilled shipping included on every bulk order we send.</p><div class="more">Read More »</div></div>

<!-- products -->
<h2 class="section-title" style="top:706px">BEST QUALITY FRESH PRODUCTS</h2>
<div class="subtitle" style="top:738px">FRESH FROM WEST AUSTRALIA, PACKED WITH CARE FOR YOUR TABLE</div>
<div class="abs arrow" style="left:232px">‹</div>
<div class="abs arrow" style="left:946px">›</div>
<div class="abs product featured" style="left:256px"><div class="photo" role="img" aria-label="Photo of red, yellow and green peppers" style="background:linear-gradient(135deg,#d8261c,#f3b41a 55%,#4c9a2a)"></div><h5>Fresh Vegetables</h5><div class="stars">★★★★★</div><div class="price">$ 35.00</div><div class="btns"><span>ADD</span><span>VIEW</span></div></div>
<div class="abs product" style="left:440px"><div class="photo" role="img" aria-label="Photo of ripe mangoes" style="background:linear-gradient(135deg,#f6b21d,#e6771a 60%,#7ea32b)"></div><h5>Fresh Fruits</h5><div class="stars">★★★★★</div><div class="price">$ 18.65</div></div>
<div class="abs product" style="left:604px"><div class="photo" role="img" aria-label="Photo of fresh oysters" style="background:linear-gradient(135deg,#8f9270,#5e6145 60%,#b7b39a)"></div><h5>Sea Food</h5><div class="stars">★★★★★</div><div class="price">$ 34.40</div></div>
<div class="abs product" style="left:768px"><div class="photo" role="img" aria-label="Photo of raw meat cuts" style="background:linear-gradient(135deg,#b2282a,#7e1a1c 60%,#d46a5c)"></div><h5>Meat</h5><div class="stars">★★★★★</div><div class="price">$ 30.85</div></div>

<!-- news -->
<div class="section-rule" style="top:1164px"><span></span></div>
<h2 class="section-title" style="top:1152px">LATEST NEWS</h2>
<div class="abs news" style="left:248px"><div class="date" style="background:var(--orange)">20<small>Jun</small></div><div class="photo" role="img" aria-label="Photo of red fish on ice" style="background:linear-gradient(135deg,#c44a2a,#e0824c)"></div></div>
<div class="abs news" style="left:484px"><div class="date" style="background:var(--teal)">14<small>Jun</small></div><div class="photo" role="img" aria-label="Photo of a bunch of dark grapes" style="background:linear-gradient(135deg,#2d2a48,#4c3d6a 60%,#5b8a30)"></div></div>
<div class="abs news" style="left:720px;background:var(--teal)"><div class="date">07<small>Jun</small></div><div class="news-text">New harvest season begins<br>with record crop yields<div style="margin-top:54px"><svg width="40" height="8"><circle cx="4" cy="4" r="3" fill="#fff"/><circle cx="14" cy="4" r="3" fill="#fff" opacity=".5"/><circle cx="24" cy="4" r="3" fill="#fff" opacity=".5"/></svg></div></div></div>

<!-- achievements -->
<div class="section-rule" style="top:1378px"><span></span></div>
<h2 class="section-title" style="top:1366px">OUR ACHIEVEMENTS</h2>
<div class="abs card member"><div class="avatar" role="img" aria-label="Illustration of a happy member"></div><div style="margin:34px 0 6px;font-size:11px;font-weight:600">1000 Member</div><div style="font-size:9px;color:var(--muted);margin-bottom:16px">Trusted by buyers</div><span class="btn">READ MORE</span></div>
<div class="abs card tabs">
  <div class="tabbar"><span class="on">Best Case</span><span>Selection</span><span>Export</span></div>
  <div class="body">
    <h4>Et harum quidem rerum facilis expedita</h4>
    <div class="count">125 : 02 : 17 : 49</div>
    <div class="count-lbl"><span>Days</span><span>Hours</span><span>Mins</span><span>Secs</span></div>
    <h4 class="small">Et harum quidem rerum facilis expedita</h4>
    <p>Our fresh produce reaches buyers in China within days of harvest, chilled and checked at every step.</p>
    <p class="link">View More</p>
  </div>
</div>
<div class="abs card offer"><h4>Fresh<br>Vegetables</h4><div class="big">$24,85</div><ul><li>› Farm picked</li><li>› Chilled transport</li><li>› Export certified</li></ul><span class="btn">READ MORE</span></div>

<!-- best products -->
<div class="section-rule" style="top:1798px"><span style="left:200px;width:320px"></span></div>
<h2 class="section-title" style="top:1786px">BUY OUR BEST PRODUCTS</h2>
<div class="abs best" style="left:248px;background:var(--orange)"><h4>Fresh Carrots</h4><div class="tag">$15</div><div class="photo" role="img" aria-label="Photo of a bunch of carrots" style="background:linear-gradient(135deg,#f27a1a,#d85a10 60%,#6aa02c)"></div></div>
<div class="abs best" style="left:486px;background:var(--lime)"><h4>Fresh Berries</h4><div class="tag">$12</div><div class="photo" role="img" aria-label="Photo of fresh blueberries" style="background:linear-gradient(135deg,#2d3f7a,#4a5f9e 60%,#2a2f55)"></div></div>
<div class="abs best" style="left:724px;background:var(--teal)"><h4>Fresh Meat</h4><div class="tag">$18</div><div class="photo" role="img" aria-label="Photo of raw steak" style="background:linear-gradient(135deg,#a52228,#d04a4a 60%,#6e1418)"></div></div>

<!-- partners -->
<div class="section-rule" style="top:2084px"><span></span></div>
<h2 class="section-title" style="top:2072px">PARTNERS</h2>
<div class="abs partner" style="left:250px"></div>
<div class="abs partner" style="left:436px"></div>
<div class="abs partner" style="left:622px"></div>
<div class="abs partner" style="left:808px"></div>

<!-- banner -->
<div class="abs banner" role="img" aria-label="Photo of a colourful market display of fruit and vegetables"></div>
<h2 class="banner-title">As Delicious As Ever</h2>
<div class="abs banner-btn">SHOP NOW</div>

<!-- tweet -->
<div class="abs tweet">
  <svg width="16" height="14" viewBox="0 0 16 14"><path d="M1 7 L15 1 L10 13 L8 8 Z" fill="#3ec5a5"/></svg>
  <span style="flex:1">Our new season citrus has landed in Shanghai, fresh and sweet. Thank you to all our growers and partners.</span>
  <span>1 month ago</span><span>‹ ›</span>
</div>

<!-- footer -->
<div class="abs footer"></div>
<div class="abs fcol" style="left:240px"><h5>SERVICES</h5><ul><li>Export</li><li>Packing</li><li>Storage</li><li>Shipping</li><li>Sourcing</li></ul></div>
<div class="abs fcol" style="left:424px"><h5>LINKS</h5><ul><li>About Us</li><li>Directors</li><li>Products</li><li>Contact</li><li>News</li></ul></div>
<div class="abs fcol" style="left:608px"><h5>PRODUCTS</h5><ul><li>Vegetables</li><li>Fruits</li><li>Seafood</li><li>Meat</li><li>Dairy</li></ul></div>
<div class="abs fcol" style="left:792px"><h5>BLOCK</h5><ul><li>Harvest</li><li>Markets</li><li>Recipes</li><li>Quality</li><li>Events</li></ul></div>
<div class="abs copy">© Copyright Greenvale. All rights reserved.</div>

</body>
</html>
```